Tovaberry LLC website and online trading portal

Beverage Manufacturing company needs a website design. Should include 5 main pages. Home, Products, About, FAQ and Contact Us. Should also include a shopping cart, online order and shipping page. Company logo is attached.

Target Market(s)

General Public, health conscious individuals

Font styles to use
Serif
Sans Serif
Script

Colors
abd037
fbee3e
ffc214
ffffff

Requirements
Must have
• e-commerce site with 5 main pages. Home, Products, About, FAQ and Contact Us. Should also include a shopping cart, online order and shipping page. Coloscheme should be derived from attached logo

```html
<!DOCTYPE html>
<html lang="en">
<head>
<meta charset="utf-8">
<title>Tovaberry — Healthy Juices</title>
<link href="https://fonts.googleapis.com/css2?family=Tinos:ital,wght@0,400;0,700;1,400&family=Dancing+Script:wght@700&display=swap" rel="stylesheet">
<style>
:root{
  --orange:#ffb229;
  --orange-deep:#f7941d;
  --cta:#ff8a00;
  --green:#7cbb13;
  --lime:#abd037;
  --yellow:#fbee3e;
  --gold:#ffc214;
  --cream:#fbf8ea;
  --card-cream:#fcebc0;
  --ink:#1d1d1d;
  --muted:#6f6f6f;
  --footer:#1b1b1b;
  --footer-text:#8c8c8c;
  --white:#ffffff;
}
*{box-sizing:border-box;margin:0;padding:0}
html,body{width:1200px;height:4434px;overflow:hidden}
body{position:relative;background:var(--white);font-family:"Tinos",serif;color:var(--ink)}
.abs{position:absolute}
a{color:inherit;text-decoration:none}

/* header */
.topbar{left:0;top:0;width:1200px;height:4px;background:var(--orange)}
.header{left:0;top:4px;width:1200px;height:68px;background:var(--white)}
.brand{left:55px;top:14px;width:103px;height:103px;background:#3a9a2c;border:3px solid var(--white);display:flex;align-items:center;justify-content:center;z-index:5}
.brand span{font-family:"Tinos",serif;font-weight:700;font-size:19px;color:var(--white)}
.nav{left:326px;top:20px;display:flex;gap:10px;align-items:center}
.nav a{font-weight:700;font-size:15px;letter-spacing:.5px;padding:8px 18px;border-radius:20px}
.nav a.active{background:var(--orange);color:var(--white)}
.tools{left:1028px;top:24px;display:flex;gap:22px}
.badge{position:absolute;right:-8px;top:-5px;width:13px;height:13px;border-radius:50%;background:var(--orange);color:#fff;font-size:9px;text-align:center;line-height:13px}

/* hero */
.hero{left:0;top:72px;width:1200px;height:534px;background:var(--orange)}
.hero-title{left:98px;top:160px;font-family:"Dancing Script",cursive;font-size:76px;color:var(--white)}
.hero-sub{left:100px;top:276px;font-size:36px;line-height:49px;color:var(--white);letter-spacing:.5px}
.hero-tag{left:98px;top:380px;font-size:60px;color:var(--white)}
.btn{display:flex;align-items:center;justify-content:center;border-radius:20px;color:var(--white);font-size:20px}
.hero-btn{left:100px;top:479px;width:157px;height:39px;background:var(--green)}
.hero-art{left:585px;top:86px;width:551px;height:508px;border-radius:40% 40% 30% 30%;background:radial-gradient(ellipse at 55% 45%,#f9d55a 0%,#f3b92a 45%,rgba(255,178,41,0) 72%)}

/* section heads */
.kicker{width:1200px;left:0;text-align:center;font-size:25px}
.heading{width:1200px;left:0;text-align:center;font-size:37px;font-weight:700}

/* categories */
.cat-band{left:0;top:606px;width:1200px;height:625px;background:var(--cream);border-radius:0 0 50% 50%/0 0 40px 40px}
.card{position:absolute;width:255px;border:1px solid #e4e4e4;background:var(--white)}
.cat-card{top:745px;height:353px}
.cat-art{position:absolute;left:6px;top:6px;width:241px;height:263px;border-radius:0 0 50% 50%/0 0 38% 38%}
.bottle{position:absolute;left:50%;transform:translateX(-50%);width:58px;border-radius:26px 26px 10px 10px}
.cat-card .bottle{top:22px;height:240px}
.cat-meta{position:absolute;left:14px;right:14px;top:304px;display:flex;justify-content:space-between;font-size:16px;font-weight:700}
.cat-meta .price{color:#9bbf1e}
.cart{position:absolute;left:50%;bottom:-20px;transform:translateX(-50%);width:40px;height:40px;border-radius:50%;background:var(--white);border:1px solid #e2e2e2;display:flex;align-items:center;justify-content:center}

/* about */
.about-art{left:103px;top:1265px;width:551px;height:526px;background:radial-gradient(ellipse at 40% 50%,#f6c230 0%,#f9d768 35%,rgba(255,255,255,0) 70%)}
.about-title{left:700px;top:1340px;width:450px;text-align:center;font-family:"Dancing Script",cursive;font-size:64px;color:var(--orange-deep)}
.about-head{left:700px;top:1443px;width:450px;text-align:center;font-size:34px;line-height:43px}
.about-text{left:722px;top:1543px;width:416px;font-size:16px;line-height:27px;color:var(--muted);text-align:center}
.about-btn{left:847px;top:1658px;width:157px;height:38px;background:var(--cta)}

/* trending */
.tr-card{height:389px}
.tr-inner{position:absolute;inset:7px;background:var(--card-cream)}
.tr-card .bottle{top:24px;height:270px}
.tr-meta{position:absolute;left:0;right:0;top:312px;text-align:center;font-weight:700;font-size:17px;line-height:22px}
.tr-meta .price{color:#e8981a}
.all-btn{left:494px;top:2877px;width:210px;height:38px;background:var(--cta)}

/* testimonial */
.testi-band{left:0;top:3068px;width:1200px;height:281px;background:var(--cream);border-radius:50% 50% 50% 50%/30px 30px 30px 30px}
.avatar{left:138px;top:3163px;width:80px;height:80px;border-radius:50%;background:linear-gradient(#e9d9c6,#c9b39b);border:4px solid var(--white);box-shadow:0 0 0 1px #e5e0d2}
.who{left:236px;top:3173px;font-size:15px;line-height:22px}
.who b{display:block}
.who i{font-size:14px}
.quote-mark{left:359px;top:3183px;width:40px;height:40px;border-radius:50%;background:#efeadb;color:#aaa;font-size:26px;text-align:center;line-height:48px}
.quote-rule{left:379px;top:3138px;width:1px;height:130px;background:#e2dccb}
.quote{left:432px;top:3172px;width:715px;font-size:14px;line-height:21px;color:#444}
.dots{left:610px;top:3279px;display:flex;gap:9px}
.dots i{width:9px;height:9px;border-radius:50%;background:#bbb}
.dots i.on{background:var(--cta)}

/* news */
.news{top:3514px;width:346px;height:348px}
.news-img{position:absolute;left:0;top:0;width:346px;height:222px}
.news-box{position:absolute;left:17px;right:17px;top:205px;height:143px;background:var(--white);box-shadow:0 3px 12px rgba(0,0,0,.08);text-align:center;padding-top:28px}
.news-box h3{font-weight:400;font-size:15px}
.news-box p{font-size:13px;line-height:19px;color:#888;margin-top:10px;letter-spacing:.4px}
.news-box a{display:block;font-size:13px;color:var(--cta);margin-top:9px}
.pager{left:520px;top:3931px;width:160px;height:1px;background:#ddd}
.arrow{top:3920px;width:22px;height:22px;border-radius:50%;border:1px solid #ccc;background:var(--white);display:flex;align-items:center;justify-content:center}

/* newsletter */
.news-band{left:0;top:3977px;width:1200px;height:109px;background:#fbb31f}
.nl-title{left:232px;top:4014px;font-size:28px;font-weight:700;color:var(--white)}
.nl-form{left:568px;top:4008px;width:439px;height:45px;background:var(--white);border-radius:23px;border:1px solid #eee}
.nl-form span{position:absolute;left:18px;top:12px;font-size:16px;color:#999}
.nl-form b{position:absolute;right:0;top:0;width:108px;height:43px;background:#111;color:#fff;border-radius:22px;font-size:16px;display:flex;align-items:center;justify-content:center}

/* footer */
.footer{left:0;top:4086px;width:1200px;height:348px;background:var(--footer)}
.f-head{top:4130px;font-size:18px;font-weight:700;color:var(--white)}
.f-about{left:53px;top:4180px;width:250px;font-size:13px;line-height:22.5px;text-align:justify;color:var(--footer-text)}
.f-links{top:4184px;font-size:14px;line-height:26.6px;color:var(--footer-text)}
.f-logo{left:752px;top:4134px;width:102px;height:100px;background:#3a9a2c;display:flex;align-items:center;justify-content:center;color:#fff;font-weight:700;font-size:17px}
.f-contact{left:875px;top:4132px;font-size:14px;line-height:25px;color:var(--footer-text)}
.f-contact li{list-style:none;display:flex;gap:12px}
.f-contact svg{flex:none;margin-top:6px}
.f-rule{left:53px;top:4372px;width:1094px;height:1px;background:#333}
.copy{left:53px;top:4394px;font-size:13px;color:var(--footer-text)}
.social{left:990px;top:4394px;display:flex;gap:22px}
.social i{width:14px;height:14px;border-radius:50%;background:#d9d9d9}
</style>
</head>
<body>

<div class="abs topbar"></div>
<header class="abs header">
  <nav class="abs nav">
    <a class="active">HOME</a><a>PRODUCTS</a><a>ABOUT</a><a>FAQ</a><a>CONTACT US</a>
  </nav>
  <div class="abs tools">
    <svg width="18" height="18" viewBox="0 0 18 18"><circle cx="7" cy="7" r="5.5" fill="none" stroke="#222" stroke-width="2"/><path d="M11 11l5 5" stroke="#222" stroke-width="2"/></svg>
    <svg width="18" height="18" viewBox="0 0 18 18"><circle cx="9" cy="5.5" r="4" fill="none" stroke="#222" stroke-width="2"/><path d="M2 17c0-4 3-6 7-6s7 2 7 6" fill="none" stroke="#222" stroke-width="2"/></svg>
    <span style="position:relative"><svg width="20" height="18" viewBox="0 0 20 18"><path d="M1 2h3l2 9h10l2-7H5" fill="none" stroke="#222" stroke-width="2"/><circle cx="8" cy="15" r="1.6" fill="#222"/><circle cx="15" cy="15" r="1.6" fill="#222"/></svg><span class="badge">0</span></span>
  </div>
</header>
<div class="abs brand"><span>Tovaberry</span></div>

<section class="abs hero"></section>
<div class="abs hero-art" role="img" aria-label="Bottle of ginger pineapple juice with fresh ginger root and pineapple slices"></div>
<h1 class="abs hero-title">Tovaberry</h1>
<p class="abs hero-sub">All the healthy benefits<br>and a delicious taste</p>
<p class="abs hero-tag">Creating Healthy</p>
<a class="abs btn hero-btn">Shop Now</a>

<!-- categories -->
<div class="abs cat-band"></div>
<p class="abs kicker" style="top:632px">- Top -</p>
<h2 class="abs heading" style="top:664px">Categories</h2>

<div class="card cat-card" style="left:52px">
  <div class="cat-art" style="background:#fbaa3a"></div>
  <div class="bottle" role="img" aria-label="Apple juice bottle" style="background:linear-gradient(#f0f0f0,#f6c45a 55%,#f1a92f)"></div>
  <div class="cat-meta"><span>Apple Juice</span><span class="price">Price: $10.00</span></div>
  <div class="cart"><svg width="16" height="15" viewBox="0 0 20 18"><path d="M1 2h3l2 9h10l2-7H5" fill="none" stroke="#222" stroke-width="2"/><circle cx="8" cy="15" r="1.6"/><circle cx="15" cy="15" r="1.6"/></svg></div>
</div>
<div class="card cat-card" style="left:332px">
  <div class="cat-art" style="background:#e2b56c"></div>
  <div class="bottle" role="img" aria-label="Ginger juice bottle with ginger root" style="background:linear-gradient(#4f9a2e,#2d6b1c)"></div>
  <div class="cat-meta"><span>Ginger Juice</span><span class="price">Price: $10.00</span></div>
  <div class="cart"><svg width="16" height="15" viewBox="0 0 20 18"><path d="M1 2h3l2 9h10l2-7H5" fill="none" stroke="#222" stroke-width="2"/><circle cx="8" cy="15" r="1.6"/><circle cx="15" cy="15" r="1.6"/></svg></div>
</div>
<div class="card cat-card" style="left:613px">
  <div class="cat-art" style="background:#8dc23c"></div>
  <div class="bottle" role="img" aria-label="Pineapple juice bottle" style="top:70px;height:190px;width:66px;background:linear-gradient(#fbd24a,#f6b21c)"></div>
  <div class="cat-meta"><span>Pineapple Juice</span><span class="price">Price: $10.00</span></div>
  <div class="cart"><svg width="16" height="15" viewBox="0 0 20 18"><path d="M1 2h3l2 9h10l2-7H5" fill="none" stroke="#222" stroke-width="2"/><circle cx="8" cy="15" r="1.6"/><circle cx="15" cy="15" r="1.6"/></svg></div>
</div>
<div class="card cat-card" style="left:893px">
  <div class="cat-art" style="background:#fbaa3a"></div>
  <div class="bottle" role="img" aria-label="Apple juice bottle" style="background:linear-gradient(#f0f0f0,#f6c45a 55%,#f1a92f)"></div>
  <div class="cat-meta"><span>Apple Juice</span><span class="price">Price: $10.00</span></div>
  <div class="cart"><svg width="16" height="15" viewBox="0 0 20 18"><path d="M1 2h3l2 9h10l2-7H5" fill="none" stroke="#222" stroke-width="2"/><circle cx="8" cy="15" r="1.6"/><circle cx="15" cy="15" r="1.6"/></svg></div>
</div>

<!-- about -->
<div class="abs about-art" role="img" aria-label="Ginger pineapple juice bottle beside ginger root and pineapple"></div>
<h2 class="abs about-title">Tovaberry</h2>
<p class="abs about-head">All the healthy benefits<br>and a delicious taste</p>
<p class="abs about-text">This is our fresh-pressed version of Lorem Ipsum. Proin gravida nibh vel velit auctor aliquet. Aenean sollicitudin, lorem quis bibendum auctor, nisi elit consequat ipsum, nec sagit-</p>
<a class="abs btn about-btn">Shop Now</a>

<!-- trending -->
<p class="abs kicker" style="top:1822px">- Shop -</p>
<h2 class="abs heading" style="top:1859px">Trending Product</h2>

<div class="card tr-card" style="left:52px;top:1958px"><div class="tr-inner"></div><div class="bottle" role="img" aria-label="Apple juice bottle" style="background:linear-gradient(#f0f0f0,#f6c45a 55%,#f1a92f)"></div><div class="tr-meta">APPLE JUICE<br><span class="price">Price: $10.00</span></div><div class="cart"><svg width="16" height="15" viewBox="0 0 20 18"><path d="M1 2h3l2 9h10l2-7H5" fill="none" stroke="#222" stroke-width="2"/><circle cx="8" cy="15" r="1.6"/><circle cx="15" cy="15" r="1.6"/></svg></div></div>
<div class="card tr-card" style="left:332px;top:1958px"><div class="tr-inner"></div><div class="bottle" role="img" aria-label="Ginger juice bottle with ginger root" style="background:linear-gradient(#4f9a2e,#2d6b1c)"></div><div class="tr-meta">GINGER JUICE<br><span class="price">Price: $10.00</span></div><div class="cart"><svg width="16" height="15" viewBox="0 0 20 18"><path d="M1 2h3l2 9h10l2-7H5" fill="none" stroke="#222" stroke-width="2"/><circle cx="8" cy="15" r="1.6"/><circle cx="15" cy="15" r="1.6"/></svg></div></div>
<div class="card tr-card" style="left:613px;top:1958px"><div class="tr-inner"></div><div class="bottle" role="img" aria-label="Pineapple juice bottle" style="top:60px;height:230px;width:66px;background:linear-gradient(#fbd24a,#f6b21c)"></div><div class="tr-meta">PINEAPPLE JUICE<br><span class="price">Price: $10.00</span></div><div class="cart"><svg width="16" height="15" viewBox="0 0 20 18"><path d="M1 2h3l2 9h10l2-7H5" fill="none" stroke="#222" stroke-width="2"/><circle cx="8" cy="15" r="1.6"/><circle cx="15" cy="15" r="1.6"/></svg></div></div>
<div class="card tr-card" style="left:893px;top:1958px"><div class="tr-inner"></div><div class="bottle" role="img" aria-label="Apple juice bottle" style="background:linear-gradient(#f0f0f0,#f6c45a 55%,#f1a92f)"></div><div class="tr-meta">APPLE JUICE<br><span class="price">Price: $10.00</span></div><div class="cart"><svg width="16" height="15" viewBox="0 0 20 18"><path d="M1 2h3l2 9h10l2-7H5" fill="none" stroke="#222" stroke-width="2"/><circle cx="8" cy="15" r="1.6"/><circle cx="15" cy="15" r="1.6"/></svg></div></div>

<div class="card tr-card" style="left:52px;top:2421px"><div class="tr-inner"></div><div class="bottle" role="img" aria-label="Apple juice bottle" style="background:linear-gradient(#f0f0f0,#f6c45a 55%,#f1a92f)"></div><div class="tr-meta">APPLE JUICE<br><span class="price">Price: $10.00</span></div><div class="cart"><svg width="16" height="15" viewBox="0 0 20 18"><path d="M1 2h3l2 9h10l2-7H5" fill="none" stroke="#222" stroke-width="2"/><circle cx="8" cy="15" r="1.6"/><circle cx="15" cy="15" r="1.6"/></svg></div></div>
<div class="card tr-card" style="left:332px;top:2421px"><div class="tr-inner"></div><div class="bottle" role="img" aria-label="Ginger juice bottle with ginger root" style="background:linear-gradient(#4f9a2e,#2d6b1c)"></div><div class="tr-meta">GINGER JUICE<br><span class="price">Price: $10.00</span></div><div class="cart"><svg width="16" height="15" viewBox="0 0 20 18"><path d="M1 2h3l2 9h10l2-7H5" fill="none" stroke="#222" stroke-width="2"/><circle cx="8" cy="15" r="1.6"/><circle cx="15" cy="15" r="1.6"/></svg></div></div>
<div class="card tr-card" style="left:613px;top:2421px"><div class="tr-inner"></div><div class="bottle" role="img" aria-label="Pineapple juice bottle" style="top:60px;height:230px;width:66px;background:linear-gradient(#fbd24a,#f6b21c)"></div><div class="tr-meta">PINEAPPLE JUICE<br><span class="price">Price: $10.00</span></div><div class="cart"><svg width="16" height="15" viewBox="0 0 20 18"><path d="M1 2h3l2 9h10l2-7H5" fill="none" stroke="#222" stroke-width="2"/><circle cx="8" cy="15" r="1.6"/><circle cx="15" cy="15" r="1.6"/></svg></div></div>
<div class="card tr-card" style="left:893px;top:2421px"><div class="tr-inner"></div><div class="bottle" role="img" aria-label="Apple juice bottle" style="background:linear-gradient(#f0f0f0,#f6c45a 55%,#f1a92f)"></div><div class="tr-meta">APPLE JUICE<br><span class="price">Price: $10.00</span></div><div class="cart"><svg width="16" height="15" viewBox="0 0 20 18"><path d="M1 2h3l2 9h10l2-7H5" fill="none" stroke="#222" stroke-width="2"/><circle cx="8" cy="15" r="1.6"/><circle cx="15" cy="15" r="1.6"/></svg></div></div>

<a class="abs btn all-btn">View all products</a>

<!-- testimonials -->
<p class="abs kicker" style="top:2975px">- What Our Consumers -</p>
<h2 class="abs heading" style="top:3011px">Say About Us</h2>
<div class="abs testi-band"></div>
<div class="abs avatar" role="img" aria-label="Customer portrait"></div>
<p class="abs who"><b>Mara Lindqvist</b><i>Co-founder</i></p>
<div class="abs quote-rule"></div>
<div class="abs quote-mark">&ldquo;</div>
<p class="abs quote">Duis Faucibus Enim Vitae Nunc Molestie, Arcu Facilisis Arcu Nullam Mattis Faucibus Enim Vitae Nunc Molestie, Need Arcu Nullam Bibendumnc Molestien Bibendum Vitae Nunc Molestie, Nec Nec Arcu Nullam Bibendum Aac,..</p>
<div class="abs dots"><i></i><i></i><i class="on"></i></div>

<!-- news -->
<p class="abs kicker" style="top:3397px">- Latest -</p>
<h2 class="abs heading" style="top:3432px">News</h2>

<article class="abs news" style="left:52px">
  <div class="news-img" role="img" aria-label="Breakfast table with fruit, cereal and milk" style="background:linear-gradient(135deg,#e9e4d8,#d9b37a 60%,#c9573c)"></div>
  <div class="news-box"><h3>Share the love</h3><p>Lorem Ipsum has been the industrys<br>standard dummy text ever since t...</p><a>Read more ›</a></div>
</article>
<article class="abs news" style="left:425px">
  <div class="news-img" role="img" aria-label="Basket of fresh bread rolls and pastries" style="background:linear-gradient(135deg,#efe7d6,#d59a52 55%,#a8672a)"></div>
  <div class="news-box"><h3>Health is wealth</h3><p>Lorem Ipsum has been the industrys<br>standard dummy text ever since t...</p><a>Read more ›</a></div>
</article>
<article class="abs news" style="left:799px">
  <div class="news-img" role="img" aria-label="Market stall full of fresh fruit and vegetables" style="background:linear-gradient(135deg,#6b4a3a,#b6483a 50%,#8a9a3a)"></div>
  <div class="news-box"><h3>Fresh is healthy</h3><p>Lorem Ipsum has been the industrys<br>standard dummy text ever since t...</p><a>Read more ›</a></div>
</article>

<div class="abs pager"></div>
<div class="abs arrow" style="left:571px"><svg width="8" height="8" viewBox="0 0 8 8"><path d="M6 0L2 4l4 4" fill="none" stroke="#333"/></svg></div>
<div class="abs arrow" style="left:602px"><svg width="8" height="8" viewBox="0 0 8 8"><path d="M2 0l4 4-4 4" fill="none" stroke="#333"/></svg></div>

<!-- newsletter -->
<div class="abs news-band"></div>
<p class="abs nl-title">Sign Up For Newsletter</p>
<div class="abs nl-form"><span>email@example.com</span><b>Subscribe</b></div>

<!-- footer -->
<footer class="abs footer"></footer>
<h4 class="abs f-head" style="left:53px">About Us</h4>
<p class="abs f-about">This is our fresh-pressed version of Lorem Ipsum. Proin gravida nibh vel velit auctor aliquet. Aenean sollicitudin, lorem quis bibendum auctor, nisi elit consequat ipsum, nec sagittis sem nibh id elit. Duis sed odio sit amet nibh vulputate cursus a sit amet mauris. Morbi accumsan ipsum velit. Nam</p>
<h4 class="abs f-head" style="left:365px">Products</h4>
<div class="abs f-links" style="left:365px">Wishlist<br>Blog<br>Faq's<br>Delivery<br>Search</div>
<h4 class="abs f-head" style="left:520px">Our Company</h4>
<div class="abs f-links" style="left:520px">Contact Us<br>Delivery<br>Terms &amp; Conditions<br>About Us<br>Legal Notice</div>
<div class="abs f-logo">Tovaberry</div>
<ul class="abs f-contact">
  <li><svg width="12" height="14" viewBox="0 0 12 14"><path d="M6 13S1 8 1 5a5 5 0 0110 0c0 3-5 8-5 8z" fill="#ddd"/><circle cx="6" cy="5" r="1.8" fill="#1b1b1b"/></svg><span>Tovaberry, 18 Orchard Lane 54321<br>Brindlewood France</span></li>
  <li><svg width="12" height="10" viewBox="0 0 12 10"><rect x=".5" y=".5" width="11" height="9" fill="none" stroke="#ddd"/><path d="M.5 .5L6 5l5.5-4.5" fill="none" stroke="#ddd"/></svg><span>sales@tovaberry.com</span></li>
  <li><svg width="12" height="12" viewBox="0 0 12 12"><path d="M2 1l2 0 1 3-1.5 1a7 7 0 003.5 3.5L8 7l3 1v2a1 1 0 01-1 1C5 11 1 7 1 2a1 1 0 011-1z" fill="#ddd"/></svg><span>(+1) 555-010-0199</span></li>
</ul>
<div class="abs f-rule"></div>
<p class="abs copy">All Rights Reserved &nbsp;|&nbsp; Copyright © 2020 tovaberry</p>
<div class="abs social"><i></i><i></i><i></i><i></i><i></i></div>

</body>
</html>
```